Web Design

We need a new website for our company. We perform several functions:

1 - IT and Network Support
2 - Computer Consultancy
3 - Cloud Services
4 - Hosted Mailvault & Online Backup
5 - Internet Connections & VOIP

Examples of some of the designs we like can be seen on:
• www.quorvex.com
• www.brintale.com

I urgently need a new website to be designed to enable me to look more professional. My competitors website is www.plmtr.co.uk

I also want to be able to look much more professional, like www.quorvex.com www.brintale.com

I have attached how I would like the website to look

Task outline
To design a home page and another internal skeleton page for a website following our requirements specification and wireframe layout/structure

Task description
We are looking for a modern, attractive, clean design for our new website to reflect our businesses professionalism and high quality services that we offer.
• www.quorvex.com
• www.brintale.com
We would like a design for a home page and one other skeleton subpage for our website. We have provided a wireframe image to assist, showing how we would like the layout/structure of our website to follow which also highlights where we would like specific content/features to go.
We have listed what features the site must have in the requirements section.
The final design should communicate to our users that we are a professional business that offer high quality services and that we are a company they can trust and rely on.

Look and feel
The wireframe we have attached is a representation of how we would like the layout and structure of the website to be designed. We would like to have a corporate theme to our website.

Colours
Open to interpretation by the designer, as long as the colours suit a corporate theme and give off a professional look and feel.

Requirements
The design must have the following:

General
• Home page design (Based on attached wireframe).
• Internal Page design (This needs to be a skeleton page which can be used for implemented the content for all over pages).

• Contact details to be visible on every page, contact number at the header and all other relative details in the footer section.
• Social networking icons within the footer section of the site.
• Avoid the use of unprofessional images for buttons, icons and banners etc.
Features desired
• Drop down navigation bar. Please see the attached image for inspiration for its design/layout.
o We would like a similar drop down menu design to the one on this site: www.plmtr.co.uk.
• Image slider at the header of every page just beneath the navigation bar.
o We would like the Talu slider to be used for the image slider. Please use this link for an example of it in action: http://www.scriptgarnet.net/demo/talu-slider/
o The image slider needs to be larger on the home page.
o The image slider can be smaller on the rest of the pages of the site.
• Chirplet feed present on every page.
• News/Blog feed present on every page.
• Call back form present on every page.
• Wendro Map implementation above footer on every page.

A user friendly, accessible design that is easy to use and easy for the user to understand. Must have a corporate theme to reflect the professionalism of our business. Content flows logically and keep content spaced out so that it does not make the site look cluttered.

Target Market(s)

Small to Mid sized Business, Large Banks and Legal, corporate, business - non-technical users

Industry/Entity Type

Business

Font styles to use
Sans Serif

```html
<!DOCTYPE html>
<html lang="en">
<head>
<meta charset="utf-8">
<title>Tallowmere Systems – IT Support</title>
<link rel="stylesheet" href="https://fonts.googleapis.com/css2?family=Montserrat:wght@300;400;600;700&family=Arimo:wght@400;700&family=Lora:ital@1&display=swap">
<style>
:root{
  --blue:#1b8ad6;
  --blue-dark:#0f6fb5;
  --blue-light:#3aa2e6;
  --ink:#333;
  --muted:#666;
  --line:#dcdcdc;
  --panel:#f3f3f3;
  --footer:#353535;
  --footer-bar:#2a2a2a;
  --white:#fff;
}
*{box-sizing:border-box;margin:0;padding:0}
html,body{width:1200px;height:2840px;overflow:hidden}
body{background:var(--white);font-family:"Arimo",Arial,sans-serif;color:var(--ink);font-size:13px;position:relative}
.abs{position:absolute}
h2.section-title{font-family:"Montserrat",sans-serif;font-weight:300;font-size:27px;letter-spacing:1px;color:#444;padding-bottom:8px;border-bottom:1px solid var(--line);position:relative}
h2.section-title::after{content:"";position:absolute;left:0;bottom:-1px;width:160px;height:2px;background:var(--blue)}

/* header */
.site-header{left:0;top:0;width:1200px;height:100px}
.brand{left:52px;top:24px;width:320px;height:50px}
.brand-name{position:absolute;left:34px;top:10px;font-family:"Montserrat",sans-serif;font-size:26px;font-weight:400;color:var(--blue)}
.brand-mark{position:absolute;left:0;top:18px;width:20px;height:20px;border-radius:50%;background:var(--blue)}
.contact-now{right:52px;top:18px;text-align:left;font-family:"Montserrat",sans-serif;color:var(--blue)}
.contact-now .label{font-size:24px;font-weight:400}
.contact-now .label b{font-weight:700}
.contact-now .phone{font-size:27px;font-weight:700;color:#1d3d5e;display:flex;align-items:center;gap:8px}
.main-nav{left:52px;top:100px;width:1096px;height:42px;border-top:1px solid var(--line);display:flex;align-items:center;font-family:"Montserrat",sans-serif;font-size:13px;color:#444}
.main-nav .item{padding:0 28px;height:30px;line-height:30px;border-right:1px solid var(--line)}
.main-nav .home{padding:0 12px 0 0}
.nav-rule{left:0;top:142px;width:1200px;height:4px;background:var(--blue)}

/* slider */
.hero{left:0;top:146px;width:1200px;height:370px;background:linear-gradient(90deg,#8f98a2 0%,#c9cfd6 35%,#e4e8ec 60%,#d6dbe0 100%)}
.hero-copy{left:708px;top:98px;width:440px;color:#222}
.hero-copy h1{font-family:"Montserrat",sans-serif;font-size:25px;font-weight:600;color:var(--blue);margin-bottom:8px}
.hero-copy p{font-size:14px;line-height:20px;margin-bottom:10px}
.tick-list{list-style:none}
.tick-list li{display:flex;align-items:center;gap:8px;font-size:14px;margin-bottom:8px}
.tick{width:18px;height:18px;flex:none}
.btn{display:inline-block;background:var(--blue);color:var(--white);font-family:"Montserrat",sans-serif;font-weight:600;font-size:13px;border-radius:4px;text-align:center}
.hero .btn{margin-top:14px;width:138px;height:42px;line-height:42px}
.slider-dots{left:562px;top:340px;display:flex;gap:6px}
.slider-dots span{width:10px;height:10px;border-radius:50%;border:1.5px solid var(--white)}
.slider-dots span.on{background:var(--white)}

/* services */
.services{left:0;top:516px;width:1200px;height:284px;background:linear-gradient(180deg,var(--blue-light),var(--blue-dark));display:flex;justify-content:center;gap:0;color:var(--white);text-align:center}
.service{width:280px;padding-top:32px}
.service .icon{width:96px;height:96px;margin:0 auto 14px;border-radius:50%;border:4px solid rgba(255,255,255,.55);background:var(--white);display:flex;align-items:center;justify-content:center}
.service h3{font-family:"Montserrat",sans-serif;font-weight:300;font-size:21px;line-height:24px}
.service p{font-size:14px;line-height:18px;margin:4px 20px 0}

/* main */
.welcome{left:52px;top:830px;width:718px}
.welcome .intro{margin-top:18px;width:440px;font-size:14px;line-height:19px}
.welcome .photo{left:468px;top:58px;width:250px;height:180px;border:1px solid var(--line);border-radius:6px;background:linear-gradient(135deg,#d9dde2,#9aa4ae)}
.welcome .tick-list{margin-top:12px}
.welcome .tick-list li{font-size:13px;margin-bottom:6px}
.body-copy{margin-top:24px;font-size:13px;line-height:18px;color:#555}
.body-copy p{margin-bottom:18px}

.feedback{left:52px;top:1600px;width:718px;height:294px;background:var(--panel);border:1px solid var(--line);border-radius:10px}
.feedback h2{position:absolute;left:28px;top:28px;width:660px;font-size:22px}
.quotes{position:absolute;left:28px;top:86px;width:660px;display:flex}
.quote{width:50%;padding:0 18px}
.quote + .quote{border-left:1px solid var(--line)}
.quote p{font-family:"Lora",serif;font-style:italic;font-size:14px;line-height:20px;color:#555}
.quote .who{display:flex;align-items:center;gap:10px;margin-top:14px}
.quote .who .mark{width:52px;height:40px;background:#e3e3e3}
.quote .who b{display:block;font-size:14px;color:var(--blue);font-weight:400}
.quote .who span{font-size:13px;color:#555}
.big-quote{position:absolute;right:48px;bottom:-30px;width:92px;height:70px}

/* sidebar */
.panel{background:var(--panel);border:1px solid var(--line);border-radius:10px}
.contact-card{left:800px;top:828px;width:348px;height:384px;padding:20px 28px}
.contact-card h2{font-size:24px}
.contact-card .lead{margin-top:12px;font-size:13px;line-height:17px}
.field{height:36px;margin-top:6px;background:var(--white);border:1px solid var(--line);border-radius:3px;font-family:"Lora",serif;font-style:italic;font-size:12px;color:#777;padding:10px 8px}
.field.first{margin-top:14px}
.field.msg{height:86px}
.contact-card .btn{position:absolute;right:28px;bottom:18px;width:102px;height:36px;line-height:36px}

.tweets{left:800px;top:1226px;width:348px;height:308px;border:1px solid var(--line);background:var(--white);font-size:11px}
.tweets .head{height:30px;display:flex;justify-content:space-between;align-items:center;padding:0 10px;border-bottom:1px solid var(--line);font-weight:700}
.tweets .follow{font-weight:400;border:1px solid #bbb;border-radius:3px;padding:2px 8px;background:#f5f5f5}
.tweet{display:flex;gap:8px;padding:8px 10px;border-bottom:1px solid #eee;height:76px}
.tweet .av{width:24px;height:24px;background:var(--blue);border-radius:3px;flex:none}
.tweet .meta{display:flex;justify-content:space-between;width:290px}
.tweet .meta b{font-size:11px}
.tweet p{margin-top:4px;color:#444;line-height:14px;width:260px}
.tweets .compose{position:absolute;left:8px;bottom:6px;width:330px;height:22px;border:1px solid #ccc;color:#999;padding:4px 6px}

.news{left:800px;top:1552px;width:348px;height:380px;padding:20px 28px}
.news h2{font-size:24px}
.news-item{margin-top:22px}
.news-item .row{display:flex;gap:14px}
.news-item .thumb{width:80px;height:60px;border-radius:3px;background:linear-gradient(135deg,#cfe2f2,#5d9bd0);flex:none}
.news-item h4{font-size:14px;color:var(--blue);font-weight:700;line-height:17px}
.news-item small{display:block;margin-top:4px;font-size:11px;color:#666}
.news-item p{margin-top:10px;font-size:13px}
.news-item p span{color:var(--blue)}
.news .btn{position:absolute;right:28px;bottom:22px;width:130px;height:36px;line-height:36px}

/* partners */
.partners{left:52px;top:1980px;width:1096px;text-align:center}
.partners h2{font-family:"Montserrat",sans-serif;font-weight:300;font-size:24px;color:#444;letter-spacing:1px}
.partners h2::after{content:"";display:block;width:62px;height:2px;background:var(--blue);margin:8px auto 0}
.badges{display:flex;justify-content:space-between;margin-top:68px}
.badges span{width:92px;height:48px;border-radius:4px;background:#d6d9dd}

.map{left:0;top:2208px;width:1200px;height:338px;background:linear-gradient(180deg,#d9d9d9,#c4c4c4)}

/* footer */
.site-footer{left:0;top:2546px;width:1200px;height:248px;background:var(--footer);color:#ddd}
.site-footer h5{font-family:"Montserrat",sans-serif;font-weight:400;font-size:19px;color:var(--white);margin-bottom:14px}
.quick{left:52px;top:38px}
.quick ul{list-style:none}
.quick li{font-size:13px;line-height:26px;display:flex;align-items:center;gap:10px}
.quick li::before{content:"";width:8px;height:8px;border-radius:50%;background:var(--blue)}
.about{left:240px;top:38px;width:520px}
.about p{font-size:13px;line-height:19px}
.about a{color:var(--blue)}
.foot-contact{left:802px;top:38px;width:346px}
.foot-contact .co{color:var(--blue);font-size:15px;margin-bottom:12px}
.foot-contact .line{display:flex;gap:12px;font-size:13px;line-height:18px;margin-bottom:12px}
.foot-contact svg{flex:none}
.social{right:52px;top:30px;display:flex;gap:10px}
.social span{width:30px;height:30px;border-radius:50%;background:#4a4a4a}
.copy-bar{left:0;top:2794px;width:1200px;height:46px;background:var(--footer-bar);color:#aaa;font-size:12px;text-align:center;line-height:46px}
.copy-bar b{color:var(--white);font-weight:400}
</style>
</head>
<body>

<header class="site-header abs">
  <div class="brand abs"><span class="brand-mark"></span><span class="brand-name">Tallowmere Systems</span></div>
  <div class="contact-now abs">
    <div class="label">CONTACT US <b>NOW</b></div>
    <div class="phone">
      <svg width="14" height="24" viewBox="0 0 14 24"><rect x="1" y="1" width="12" height="22" rx="2" fill="none" stroke="#1b8ad6" stroke-width="2"/><circle cx="7" cy="19" r="1.5" fill="#1b8ad6"/></svg>
      +44 141 555 0192
    </div>
  </div>
</header>

<nav class="main-nav abs">
  <span class="item home"><svg width="18" height="16" viewBox="0 0 18 16"><path d="M9 1 1 8h2v7h4v-5h4v5h4V8h2z" fill="#333"/></svg></span>
  <span class="item">PRODUCTS ▾</span>
  <span class="item">COMPANY</span>
  <span class="item">BLOG</span>
  <span class="item" style="border-right:0">CONTACT US</span>
</nav>
<div class="nav-rule abs"></div>

<section class="hero abs" role="img" aria-label="Photo of business people in a video conference meeting">
  <div class="hero-copy abs">
    <h1>INTERNET CONNECTIONS &amp; VOIP</h1>
    <p>Lorem ipsum dolor sit amet consectetur adipis cing elit ut sit amet metus ut lorem consectetur adipis cing.</p>
    <ul class="tick-list">
      <li><svg class="tick" viewBox="0 0 18 18"><circle cx="9" cy="9" r="9" fill="#1b8ad6"/><path d="M5 9l3 3 5-6" stroke="#fff" stroke-width="2" fill="none"/></svg>Lorem ipsum dolor sit amet, consectetur</li>
      <li><svg class="tick" viewBox="0 0 18 18"><circle cx="9" cy="9" r="9" fill="#1b8ad6"/><path d="M5 9l3 3 5-6" stroke="#fff" stroke-width="2" fill="none"/></svg>Adipis cing elit ut sit amet metus ut lorem</li>
    </ul>
    <span class="btn">LEARN MORE</span>
  </div>
  <div class="slider-dots abs"><span></span><span></span><span></span><span></span><span class="on"></span></div>
</section>

<section class="services abs">
  <div class="service">
    <div class="icon"><svg width="48" height="48" viewBox="0 0 48 48"><circle cx="24" cy="24" r="13" fill="none" stroke="#1b8ad6" stroke-width="8" stroke-dasharray="6 4"/><circle cx="24" cy="24" r="5" fill="#1b8ad6"/></svg></div>
    <h3>IT SUPPORT</h3>
    <p>Lorem ipsum dolor sit amet, consectetur adipiscing elit. Ut sit amet metus ut lorem pharetr.</p>
  </div>
  <div class="service">
    <div class="icon"><svg width="48" height="48" viewBox="0 0 48 48"><rect x="8" y="8" width="32" height="32" rx="5" fill="#1b8ad6"/><path d="M17 31l2-6 10-10 4 4-10 10z" fill="#fff"/></svg></div>
    <h3>FREE NETWORK AUDIT</h3>
    <p>Lorem ipsum dolor sit amet, consectetur adipiscing elit. Ut sit amet metus ut lorem pharetr.</p>
  </div>
  <div class="service">
    <div class="icon"><svg width="50" height="40" viewBox="0 0 50 40"><path d="M12 34a9 9 0 0 1 0-18 12 12 0 0 1 23-3 10 10 0 0 1 3 21z" fill="#1b8ad6"/><path d="M25 30V17m-6 6 6-6 6 6" stroke="#fff" stroke-width="3" fill="none"/></svg></div>
    <h3>BACKUP &amp; CLOUD<br>SOLUTIONS</h3>
    <p>Lorem ipsum dolor sit amet, consectetur adipiscing elit. Ut sit amet metus ut lorem pharetr.</p>
  </div>
  <div class="service">
    <div class="icon"><svg width="48" height="48" viewBox="0 0 48 48"><circle cx="24" cy="24" r="20" fill="#1b8ad6"/><path d="M13 19h20m-5-5 5 5-5 5M35 29H15m5-5-5 5 5 5" stroke="#fff" stroke-width="3" fill="none"/></svg></div>
    <h3>HOSTED MAILVAULT</h3>
    <p>Lorem ipsum dolor sit amet, consectetur adipiscing elit. Ut sit amet metus ut lorem pharetr.</p>
  </div>
</section>

<main>
  <section class="welcome abs">
    <h2 class="section-title">WELCOME</h2>
    <div class="photo abs" role="img" aria-label="Photo of hands typing on a laptop beside a magnifying glass"></div>
    <p class="intro">For many companies today, IT support is a large part of doing business. It is not always possible for a company or business to have a dedicated IT support team. For companies/businesses in Glasgow, Scotland, the answer for IT needs is Tallowmere Systems Limited.</p>
    <ul class="tick-list">
      <li><svg class="tick" viewBox="0 0 18 18"><circle cx="9" cy="9" r="9" fill="#1b8ad6"/><path d="M5 9l3 3 5-6" stroke="#fff" stroke-width="2" fill="none"/></svg>Lorem ipsum dolor sit amet, consectetur adipiscing elit.</li>
      <li><svg class="tick" viewBox="0 0 18 18"><circle cx="9" cy="9" r="9" fill="#1b8ad6"/><path d="M5 9l3 3 5-6" stroke="#fff" stroke-width="2" fill="none"/></svg>Pellentesque rhoncus magna in tellus luctus gravida.</li>
      <li><svg class="tick" viewBox="0 0 18 18"><circle cx="9" cy="9" r="9" fill="#1b8ad6"/><path d="M5 9l3 3 5-6" stroke="#fff" stroke-width="2" fill="none"/></svg>Pellentesque congue purus vitae ante</li>
    </ul>
    <div class="body-copy">
      <p>Etiam tempus est quis massa sagittis sit amet lobortis quam malesuada. In interdum blandit ornare. Vivamus malesuada arcu in tellus consectetur rhoncus. Lorem ipsum dolor sit amet, consectetur adipiscing elit. Pellentesque rhoncus.</p>
      <p>Magna in tellus luctus gravida. Donec nisi diam, imperdiet eu pulvinar eget, faucibus eu mi. Integer velit erat, blandit a ullamcorper id, volutpat et quam.</p>
      <p>Maecenas ultrices eros eget justo ultricies in mollis augue commodo. Nullam sem tortor, volutpat non eleifend ut, adipiscing in augue. Aliquam at eros magna. Etiam tempus est quis massa sagittis sit amet lobortis quam malesuada. In interdum blandit ornare. Vivamus malesuada arcu in tellus consectetur rhoncus. Lorem ipsum dolor sit amet, consectetur adipiscing elit. Pellentesque rhoncus magna in tellus luctus gravida. Donec nisi diam, imperdiet eu pulvinar eget, faucibus eu mi. Integer velit erat, blandit a ullamcorper id, volutpat et quam. Cras ornare volutpat nibh sit amet malesuada. Proin sit amet leo orci, eu molestie risus. Quisque in magna sem. Integer in tellus felis. Donec nisl nibh, condimentum et ornare ac, rhoncus a urna.</p>
      <p>Nulla vehicula lobortis metus vitae venenatis. In condimentum placerat scelerisque. Sed tellus erat, pellentesque sit amet elementum quis, ultricies ut sapien. Donec vehicula egestas sollicitudin. Mauris suscipit rutrum dignissim. Sed vitae libero eget erat tincidunt condimentum eget quis mauris. Aliquam gravida blandit velit, vitae placerat lacus vulputate nec. Pellentesque in orci id est venenatis tristique. Ut in arcu nec nisi sollicitudin adipiscing nec sit amet urna. Maecenas pharetra auctor magna, vitae consectetur tortor iaculis at.</p>
      <p>Cum sociis natoque penatibus et magnis dis parturient montes, nascetur ridiculus mus. Proin suscipit nisi non eros malesuada dapibus non vel nulla. Donec quam massa, aliquam at rhoncus laoreet.</p>
    </div>
  </section>

  <section class="feedback abs">
    <h2 class="section-title">CLIENTS FEEDBACK</h2>
    <div class="quotes">
      <div class="quote">
        <p>We have used Tallowmere Systems Ltd for many IT services across a number of companies that I have been involved with. They are dedicated professionals who always delivers results in a timely manner.</p>
        <div class="who"><span class="mark"></span><div><b>Alan Brodie</b><span>KLN Leeds</span></div></div>
      </div>
      <div class="quote">
        <p>Tallowmere Systems, are smart, intuitive, structured and analytical thinkers who provides great advice and valuable support – always in a cheerful and positive manner.</p>
        <div class="who"><span class="mark"></span><div><b>Morag P</b><span>Northfield Ventures</span></div></div>
      </div>
    </div>
    <svg class="big-quote" viewBox="0 0 92 70"><path d="M8 0h30v34L22 70H6l12-34H8zM54 0h30v34L68 70H52l12-34H54z" fill="#1b8ad6"/></svg>
  </section>

  <aside>
    <section class="contact-card panel abs">
      <h2 class="section-title">CONTACT US</h2>
      <p class="lead">We guarantee to respond within one hour<br>Alternatively call us on: 0141 555 0192</p>
      <div class="field first">Insert Your Name</div>
      <div class="field">Insert Your Email</div>
      <div class="field">Insert Your Phone Number</div>
      <div class="field msg">Insert Your Message</div>
      <span class="btn">SUBMIT</span>
    </section>

    <section class="tweets abs">
      <div class="head">Tweets <span class="follow">Follow</span></div>
      <div class="tweet"><span class="av"></span><div><div class="meta"><b>Tallowmere Systems</b><span>5 Oct 13</span></div><span>@tallowmere_IT</span><p>Clean Light is a great free font designed by @corvin_lake. Check it out now</p></div></div>
      <div class="tweet"><span class="av"></span><div><div class="meta"><b>Tallowmere Systems</b><span>25 Jun 12</span></div><span>@tallowmere_IT</span><p>This is a test message</p></div></div>
      <div class="tweet"><span class="av"></span><div><div class="meta"><b>Tallowmere Systems</b><span>10 Feb 12</span></div><span>@tallowmere_IT</span></div></div>
      <div class="compose">Tweet to @tallowmere_IT</div>
    </section>

    <section class="news panel abs">
      <h2 class="section-title">LATEST NEWS</h2>
      <div class="news-item">
        <div class="row"><span class="thumb" role="img" aria-label="Illustration for news article"></span><div><h4>Why Our Competitors Hate Us....</h4><small>March 11, 2014 By Site Admin</small></div></div>
        <p>When you hire IT Consultants from us, we give you <span>[...]</span></p>
      </div>
      <div class="news-item">
        <div class="row"><span class="thumb" role="img" aria-label="Illustration of cloud software"></span><div><h4>7 Reasons Small Businesses Switch to Cloud Based Software</h4><small>March 11, 2014 By Site Admin</small></div></div>
        <p>When you hire IT Consultants from us, we give you <span>[...]</span></p>
      </div>
      <span class="btn">SEE ALL NEWS</span>
    </section>
  </aside>

  <section class="partners abs">
    <h2>OUR PARTNERS</h2>
    <div class="badges"><span></span><span></span><span></span><span></span><span></span><span></span><span></span><span></span><span></span></div>
  </section>

  <section class="map abs" role="img" aria-label="Wendro Map of Glasgow and surrounding area"></section>
</main>

<footer class="site-footer abs">
  <div class="quick abs">
    <h5>QUICK LINKS</h5>
    <ul><li>Home</li><li>Products</li><li>Company</li><li>Blog</li><li>Contact Us</li></ul>
  </div>
  <div class="about abs">
    <h5>ABOUT US</h5>
    <p>Tallowmere Systems Limited provide Business IT Support to companies in Glasgow and beyond. Some of our services include Managed IT Support, Hosted Mailvault, Online backup and Cloud Solutions <a>Read More</a></p>
  </div>
  <div class="foot-contact abs">
    <h5>CONTACT US</h5>
    <div class="co">Tallowmere Systems Limited</div>
    <div class="line"><svg width="14" height="20" viewBox="0 0 14 20"><path d="M7 0a7 7 0 0 0-7 7c0 5 7 13 7 13s7-8 7-13a7 7 0 0 0-7-7zm0 10a3 3 0 1 1 0-6 3 3 0 0 1 0 6z" fill="#ddd"/></svg><span>14 -16 Mill Lane<br>Kelso,<br>TD7 4QX</span></div>
    <div class="line"><svg width="14" height="16" viewBox="0 0 14 16"><path d="M3 0l3 4-2 2c1 2 3 4 5 5l2-2 3 3-2 3C6 15-1 8 0 2z" fill="#ddd"/></svg><span>+44 141 555 0192</span></div>
    <div class="line"><svg width="16" height="12" viewBox="0 0 16 12"><rect width="16" height="12" fill="#ddd"/><path d="M0 0l8 7 8-7" stroke="#353535" fill="none"/></svg><span style="color:var(--blue)">info@tallowmere-systems.com</span></div>
  </div>
  <div class="social abs"><span></span><span></span><span></span><span></span></div>
</footer>
<div class="copy-bar abs">Copyright © 2014 Tallowmere Systems Limited. All Rights Reserved. <b>Privacy Policy</b> | <b>Site Map</b></div>

</body>
</html>
```